Web Design Project

My website was fine - years ago. But it's way, way overdue for an overhaul. When I started my business almost 20 years ago, I wanted to be edgy. And my website was just that. Color, style, voice. Edgy. Today, my clients are corporations. I'm older, more experienced - but still a little edgy. It's controlled edge. What I want now is sophisticated. Savvy. Corporate but cool. Grown up.

My clients are primarily - but not exclusively - in healthcare. But I don't want a healthcare site. I provide the following services:
1. Writing - white papers, brochures, web pages, speechwriting, etc.
2. Marketing strategy
3. Public relations services
4. Thought leader development
5. Training
I couldn't upload all the icons but I can send them. They correspond with the pages as follows and should be used in the design:

1. Writing- nib.png
2. Marketing strategy-compass.png
3. Public relations services-microphone.png
4. Thought leader development-lightbulb.png
5. Training: cogs-training.png or key.png

I will have a blog, and a portfolio of some kind.

I don't want something that looks like a template.
Updates

Reason: Just made this a committed payment. I apologize for not doing so from the start. Nobody should work for free.

Reason: Several folks have asked to resubmit, and it has taken me a while to provide feedback.

Dear Designers,

I am so sorry to have been so slow to select. I've had professional and personal issues to deal with. I am actively trying to select a design, however, and will do so in the next two days. Thanks so much for your patience and hard work.

Rhoda

Thanks so much to everyone who has submitted a design. I had great luck crowdsourcing my logo, but I'm starting to realize that website design is a totally different animal. All of your designs are great, but they all look exactly like templates. And maybe that's the way it's supposed to be, the way it should be. I don't want to use stock photography. It needs to be more personalized than that. I'm open to illustration or even using my own photo on the site, but stock photography won't work for me. If anyone wants to submit something else - and I understand if you don't - please feel free. 

Target Market(s)

C-suite executives; corporations, larger businesses who need marketing writing

Industry/Entity Type

Healthcare

Requirements
Must have
• Logo (somewhere)
Icons
Nice to have
• Level-specific page design (e.g, Home = Level 1, Tabs = Level 2, etc). I'd like it to have a certain order.

```html
<!DOCTYPE html>
<html lang="en">
<head>
<meta charset="utf-8">
<title>The Crux – Marketing Communications</title>
<link href="https://fonts.googleapis.com/css2?family=Source+Sans+3:ital,wght@0,400;0,600;0,700;1,600;1,700&family=PT+Sans+Narrow:wght@700&display=swap" rel="stylesheet">
<style>
  :root{
    --purple:#5b2a86;
    --purple-dark:#4a1f70;
    --orange:#e8820e;
    --paper:#f3f3f1;
    --card:#ffffff;
    --ink:#333333;
    --ink-soft:#555555;
    --grey-band:#e2e2e2;
    --footer:#333333;
    --rule:#cfcfcf;
  }
  *{box-sizing:border-box;margin:0;padding:0}
  html,body{width:711px;height:1200px;overflow:hidden}
  body{position:relative;background:var(--paper);font-family:"Source Sans 3",Arial,sans-serif;color:var(--ink)}
  .abs{position:absolute}

  /* Header */
  .brand{left:62px;top:21px;width:130px}
  .brand-mark{position:absolute;left:46px;top:0;width:30px;height:30px;background:var(--orange)}
  .brand-name{position:absolute;left:0;top:40px;font-size:25px;font-weight:600;color:var(--purple);letter-spacing:1px;white-space:nowrap}
  .brand-tagline{position:absolute;left:0;top:71px;font-size:5px;color:var(--purple);letter-spacing:.4px;white-space:nowrap;text-transform:uppercase}
  .social{right:62px;top:20px;display:flex;gap:4px}
  .social span{width:19px;height:19px;border-radius:50%;background:var(--purple)}
  .call{right:62px;top:54px;font-size:11px;color:var(--ink)}

  /* Navigation */
  .main-nav{left:62px;top:100px;width:123px;list-style:none}
  .main-nav li{height:26.7px;line-height:26px;font-size:11px;color:var(--ink);border-bottom:1px solid var(--rule);padding-left:0;position:relative}
  .main-nav li::after{content:"›";position:absolute;right:6px;top:0;color:#999;font-size:13px}
  .main-nav li:last-child{border-bottom:none}
  .main-nav li.active{background:var(--purple);color:#fff;padding-left:7px;border-bottom:none}
  .main-nav li.active::after{color:#fff}

  /* Hero */
  .hero-rule{left:200px;width:449px;height:1px;background:var(--purple)}
  .hero-photo{left:391px;top:71px;width:258px;height:256px;background:radial-gradient(ellipse at 55% 40%,#e9e9e9 0%,#bdbdbd 55%,#8d8d8d 100%)}
  .hero-title{left:217px;top:140px;font-size:20px;color:var(--orange)}
  .hero-copy{left:217px;top:171px;font-size:15px;line-height:18px;color:var(--ink)}
  .btn-primary{left:217px;top:217px;width:90px;height:23px;background:var(--purple);color:#fff;font-size:11px;line-height:23px;text-align:center;border-radius:2px}
  .slider-dots{left:217px;top:295px;display:flex;gap:3px}
  .slider-dots span{width:10px;height:10px;border-radius:50%;background:var(--orange)}
  .slider-dots span:first-child{background:var(--purple)}

  /* Welcome */
  .section-title{left:0;width:711px;text-align:center;font-size:17px;font-weight:700;color:var(--purple)}
  .section-sub{left:0;width:711px;text-align:center;font-size:10.5px;color:var(--purple)}

  /* Services */
  .services{left:62px;top:414px;width:587px;display:flex;justify-content:space-between}
  .service{position:relative;width:108px;height:180px}
  .service-card{position:absolute;left:0;top:50px;width:108px;height:130px;background:var(--card);border-radius:4px}
  .service-icon{position:absolute;left:12px;top:0;width:84px;height:84px;border-radius:50%;background:var(--purple);border:3px solid var(--orange);box-shadow:0 0 0 2px var(--purple)}
  .service h3{position:absolute;left:0;top:96px;width:108px;text-align:center;font-size:10px;font-style:italic;font-weight:700;color:var(--ink)}
  .service p{position:absolute;left:10px;top:119px;width:88px;text-align:center;font-size:8px;line-height:10px;color:var(--ink-soft)}
  .btn-more{display:inline-block;width:31px;height:13px;background:var(--ink);color:#fff;font-size:8px;line-height:13px;text-align:center;border-radius:2px}
  .service .btn-more{position:absolute;left:38px;top:158px}

  /* Portfolio */
  .portfolio{left:0;top:678px;width:711px;height:189px;background:var(--orange)}
  .arrow-box{position:absolute;top:61px;width:44px;height:34px;background:#fff}
  .arrow-box svg{position:absolute;left:14px;top:9px}
  .work{position:absolute;top:22px;width:124px}
  .work-thumb{width:124px;height:94px;border:4px solid #fff}
  .work h4{margin-top:10px;text-align:center;font-size:10.5px;font-weight:700;color:#fff}
  .work p{margin-top:4px;text-align:center;font-size:8px;line-height:10px;color:#fff}

  /* Info columns */
  .info{left:0;top:867px;width:711px;height:195px;background:var(--grey-band)}
  .col{position:absolute;top:20px;width:170px;height:175px}
  .col h2{font-family:"PT Sans Narrow",sans-serif;font-size:13.5px;font-weight:700;color:var(--ink);text-transform:uppercase;line-height:15px}
  .col h5{font-family:"PT Sans Narrow",sans-serif;font-size:11px;font-weight:700;color:var(--ink);line-height:13px}
  .col p{font-size:8px;line-height:10px;color:var(--ink-soft)}
  .col .btn-more{position:absolute;left:0;top:138px}
  .portrait{float:left;width:50px;height:46px;margin:0 6px 2px 0;background:linear-gradient(135deg,#6b4a35,#c9a27e)}
  .posts{list-style:none;margin-top:14px}
  .posts li{display:flex;gap:8px;align-items:center;padding:4px 0;border-bottom:1px solid var(--rule);width:162px}
  .posts li:last-child{border-bottom:none}
  .posts b{flex:none;width:20px;height:17px;background:var(--ink);color:#fff;font-size:11px;font-weight:400;line-height:17px;text-align:center}

  /* Footer */
  .site-footer{left:0;top:1062px;width:711px;height:138px;background:var(--footer);color:#fff}
  .badge{position:absolute;left:62px;top:22px;width:30px;height:30px;border-radius:50%;background:#555;border:2px solid #777}
  .badge-text{position:absolute;left:98px;top:30px;font-size:11px;font-weight:700;color:#888}
  .copyright{position:absolute;left:62px;top:58px;font-size:8px;color:#ddd}
  .footer-social{position:absolute;left:62px;top:86px;display:flex;gap:4px}
  .footer-social span{width:19px;height:19px;border-radius:50%;background:#666}
  .footer-nav{position:absolute;right:62px;top:21px;display:flex;gap:14px;font-size:8px;color:#fff;list-style:none}
  .address{position:absolute;right:62px;top:47px;font-size:11px}
  .phone{position:absolute;right:62px;top:73px;font-size:14px;color:var(--orange)}
  .email{position:absolute;right:62px;top:92px;font-size:11px}
</style>
</head>
<body>

<header>
  <div class="abs brand">
    <span class="brand-mark"></span>
    <div class="brand-name">THE CRUX</div>
    <div class="brand-tagline">communications that get to it</div>
  </div>
  <div class="abs social" aria-label="Social links"><span></span><span></span><span></span></div>
  <div class="abs call">Call Now :&nbsp; +1 555 210 4417</div>
</header>

<nav>
  <ul class="abs main-nav">
    <li>What's the Crux</li>
    <li class="active">Why the Crux?</li>
    <li>Folks Who Dig Us</li>
    <li>What We Do</li>
    <li>The Proof</li>
    <li>What's Up</li>
    <li>Who's Running Things</li>
    <li>Did You Know</li>
    <li>Contact Us</li>
  </ul>
</nav>

<section class="hero">
  <div class="abs hero-rule" style="top:89px"></div>
  <div class="abs hero-photo" role="img" aria-label="Black and white portrait of a smiling professional woman in glasses"></div>
  <div class="abs hero-rule" style="top:327px"></div>
  <h1 class="abs hero-title" style="font-weight:400">Big words, Simple idea</h1>
  <p class="abs hero-copy">We develop marketing and PR<br>plans that work</p>
  <div class="abs btn-primary">Know The Crux</div>
  <div class="abs slider-dots"><span></span><span></span><span></span><span></span></div>
</section>

<section>
  <h2 class="abs section-title" style="top:353px">Hello and welcome to our site!</h2>
  <p class="abs section-sub" style="top:375px">The Crux is an independent marketing communications and public relations writing and consulting firm</p>

  <div class="abs services">
    <div class="service"><div class="service-card"></div><div class="service-icon" role="img" aria-label="Compass icon"></div><h3>Marketing strategy</h3><p>Praesent vestibulum molestie lacus. Aenean nonummy hendrerit .</p><span class="btn-more">More</span></div>
    <div class="service"><div class="service-card"></div><div class="service-icon" role="img" aria-label="Cogs icon"></div><h3>Public relations</h3><p>Praesent vestibulum molestie lacus. Aenean nonummy hendrerit .</p><span class="btn-more">More</span></div>
    <div class="service"><div class="service-card"></div><div class="service-icon" role="img" aria-label="Lightbulb icon"></div><h3>Thought leader</h3><p>Praesent vestibulum molestie lacus. Aenean nonummy hendrerit .</p><span class="btn-more">More</span></div>
    <div class="service"><div class="service-card"></div><div class="service-icon" role="img" aria-label="Key icon"></div><h3>Training</h3><p>Praesent vestibulum molestie lacus. Aenean nonummy hendrerit .</p><span class="btn-more">More</span></div>
    <div class="service"><div class="service-card"></div><div class="service-icon" role="img" aria-label="Compass icon"></div><h3>Writing</h3><p>Praesent vestibulum molestie lacus. Aenean nonummy hendrerit .</p><span class="btn-more">More</span></div>
  </div>

  <h2 class="abs section-title" style="top:621px">Our latest work!</h2>
  <p class="abs section-sub" style="top:641px">Go ahead, cruise our site. Then give us a call or fire off an email if there's anything we can do for you.</p>
</section>

<section class="abs portfolio">
  <div class="arrow-box" style="left:60px"><svg width="16" height="16" viewBox="0 0 16 16"><path d="M11 2 L5 8 L11 14" fill="none" stroke="#e8820e" stroke-width="3.5"/></svg></div>
  <div class="arrow-box" style="left:605px"><svg width="16" height="16" viewBox="0 0 16 16"><path d="M5 2 L11 8 L5 14" fill="none" stroke="#e8820e" stroke-width="3.5"/></svg></div>

  <div class="work" style="left:146px">
    <div class="work-thumb" role="img" aria-label="City skyline at night reflected in water" style="background:linear-gradient(180deg,#1a1d2a 0%,#3a3a48 55%,#a07a3a 80%,#1b1b22 100%)"></div>
    <h4>Portfolio website</h4><p>Praesent vestibulum molestie lacus.<br>Aenean nonummy hendrerit .</p>
  </div>
  <div class="work" style="left:292px">
    <div class="work-thumb" role="img" aria-label="Blue water droplets close-up" style="background:linear-gradient(135deg,#0a4fb0 0%,#2d8be0 50%,#0b3f8f 100%)"></div>
    <h4>Company writing</h4><p>Praesent vestibulum molestie lacus.<br>Aenean nonummy hendrerit .</p>
  </div>
  <div class="work" style="left:437px">
    <div class="work-thumb" role="img" aria-label="Butterfly resting on pink flowers" style="background:linear-gradient(135deg,#c8457f 0%,#d9b08a 45%,#5f8a3a 100%)"></div>
    <h4>Fashion Portfolio</h4><p>Praesent vestibulum molestie lacus.<br>Aenean nonummy hendrerit .</p>
  </div>
</section>

<section class="abs info">
  <div class="col" style="left:63px">
    <h2>Who's running things</h2>
    <h5>Rhoda Marlowe, principal.</h5>
    <div style="margin-top:14px">
      <div class="portrait" role="img" aria-label="Portrait photo of the principal"></div>
      <p>Rhoda Marlowe is a seasoned communications and public relations professional with more than a decade of experience, much of it in high tech. Both a skilled writer and strategist, Marlowe is uniquely able to both plan and deliver creative, strategic materials..</p>
    </div>
    <span class="btn-more">More</span>
  </div>

  <div class="col" style="left:268px">
    <h2>Latest blog posts</h2>
    <h5>Recent posts and articles from our blog.</h5>
    <ul class="posts">
      <li><b>01</b><p>Sed ut perspiciatis unde omnis iste natus error sit voluptatem.</p></li>
      <li><b>02</b><p>eaque ipsa quae ab illo inore veritatis et quasi architecto.</p></li>
      <li><b>03</b><p>sed quia consequuntur magores eos qui ratione voluptatem.</p></li>
    </ul>
    <span class="btn-more">More</span>
  </div>

  <div class="col" style="left:475px">
    <h2>In the press</h2>
    <h5>Awarded with WBLC Certification</h5>
    <p style="margin-top:14px">Atlanta --The Crux Communications, LLC, an Atlanta-based marketing communications/PR writing firm, proudly announces its certification as a Women's Business Enterprise (WBE) by the Women's Business Leadership Council (WBLC). The Crux is one of only 10 Georgia marketing consulting services companies with this certification status.</p>
    <span class="btn-more">More</span>
  </div>
</section>

<footer class="abs site-footer">
  <div class="badge" role="img" aria-label="Certification badge"></div>
  <div class="badge-text">WBLC Certified</div>
  <p class="copyright">© copyrights The Crux Communications Inc. All rights reserved</p>
  <div class="footer-social"><span></span><span></span><span></span></div>
  <ul class="footer-nav"><li>Home</li><li>About the crux</li><li>Our services</li><li>Press</li><li>Contact us</li></ul>
  <p class="address">48 Linden Row, Suite 5, Fairview 30999</p>
  <p class="phone">Phone: 1-555-210-4417</p>
  <p class="email">E-mail: rmarlowe@cruxcomm.example</p>
</footer>

</body>
</html>
```